Business Stationery - Business Cards - Letterheads, Compliment Slips

We need a new set of artwork designed for our client, they are a Construction Company, that also sell Kitchens, bathrooms and appliances.
They are an up and comping company that focus on quality and bespoke build. For them it is all about the quality of what they install, build or design. They have recently been awarded sole distributorship of a German kitchen brand Annelore Kuchen.
We need to present a quick job to them and provide some proofs for their new Artwork which encompasses all the elements of the company
The company name is the Halvorn Group and we need to design a logo also.
Any Questions please let me know asap

Target Market(s)
Upmarket clients, or small Development companies.
Industry/Entity Type
Business
Look and feel

```html
<!DOCTYPE html>
<html lang="en">
<head>
<meta charset="utf-8">
<title>Halvorn Group – Stationery</title>
<link rel="stylesheet" href="https://fonts.googleapis.com/css2?family=Cormorant+Garamond:wght@500&family=Tinos&display=swap">
<style>
:root{
  --ink:#3d3835;
  --gold:#a8a46a;
  --gold-light:#c9c58e;
  --gold-dark:#8c874f;
  --paper:#ffffff;
  --floor:#e9e6e1;
  --line:#8a8a8a;
  --text-dark:#2b2826;
  --text-light:#ece9e2;
}
*{margin:0;padding:0;box-sizing:border-box}
html,body{width:1200px;height:3600px;overflow:hidden}
body{background:var(--paper);font-family:"Tinos",serif;position:relative}
.wordmark{font-family:"Cormorant Garamond",serif;font-weight:500;color:var(--gold);text-align:center;line-height:1;text-transform:uppercase;white-space:nowrap}
.wordmark .top,.wordmark .bottom{display:block}

/* section 1 */
.brand-panel{position:absolute;left:0;top:0;width:1200px;height:996px;background:var(--ink)}
.brand-panel .wordmark{position:absolute;left:0;right:0;top:520px}
.brand-panel .top{font-size:140px;letter-spacing:20px;padding-left:20px}
.brand-panel .bottom{font-size:92px;letter-spacing:32px;padding-left:32px;margin-top:8px}
.brand-panel .mark-square{position:absolute;left:690px;top:250px;width:160px;height:160px;background:var(--gold)}

/* section 2 cards */
.card-scene{position:absolute;left:0;top:996px;width:1200px;height:1008px;background:var(--floor)}
.card{position:absolute;top:190px;width:380px;height:630px;background:var(--ink);box-shadow:0 8px 18px rgba(0,0,0,.25)}
.card-front{left:170px}
.card-back{left:650px}
.card .band{position:absolute;left:0;right:0;bottom:0;height:28px;background:linear-gradient(90deg,var(--gold-dark),var(--gold-light))}
.card-front .name{position:absolute;top:200px;left:0;right:0;text-align:center;color:var(--text-light);font-size:26px;letter-spacing:1px}
.card-front .role{position:absolute;top:234px;left:0;right:0;text-align:center;color:var(--text-light);font-size:16px;font-style:italic}
.card-front .mini-square{position:absolute;left:165px;top:70px;width:50px;height:50px;background:var(--gold)}
.contact-stack{position:absolute;top:340px;left:0;right:0;text-align:center;color:var(--text-light);font-size:17px}
.contact-stack .item{display:flex;flex-direction:column;align-items:center;gap:6px;margin-bottom:14px}
.card-back .mark-square{position:absolute;left:240px;top:170px;width:60px;height:60px;background:var(--gold)}
.card-back .wordmark{position:absolute;left:0;right:0;top:255px}
.card-back .top{font-size:52px;letter-spacing:5px;padding-left:5px}
.card-back .bottom{font-size:34px;letter-spacing:11px;padding-left:11px;margin-top:4px}
.icon{width:20px;height:20px;display:block}

/* section 3 letterheads */
.letterhead-panel{position:absolute;left:0;top:2004px;width:1200px;height:936px;background:var(--ink)}
.letterhead{position:absolute;top:89px;width:557px;height:782px;background:var(--paper)}
.letterhead-a{left:36px}
.letterhead-b{left:612px}
.letterhead .tab{position:absolute;right:24px;top:0;width:110px;height:124px;background:var(--ink);overflow:hidden}
.letterhead .tab .mark-square{position:absolute;left:72px;top:18px;width:26px;height:26px;background:var(--gold)}
.letterhead .tab .wordmark{position:absolute;left:0;right:0;top:62px}
.letterhead .tab .top{font-size:17px;letter-spacing:1px;padding-left:1px}
.letterhead .tab .bottom{font-size:12px;letter-spacing:4px;padding-left:4px;margin-top:3px}
.letterhead .footer{position:absolute;left:22px;right:22px;bottom:26px;display:flex;align-items:center;gap:10px;font-size:9px;color:var(--text-dark)}
.letterhead .footer-rule{position:absolute;left:22px;right:22px;bottom:18px;height:5px;background:linear-gradient(90deg,var(--gold-dark),var(--gold-light))}
.footer .item{display:flex;align-items:center;gap:3px;white-space:nowrap}
.footer .icon{width:11px;height:11px}

/* section 4 compliment slip */
.slip{position:absolute;left:36px;top:3000px;width:1128px;height:540px;background:var(--paper);border:2px solid var(--ink)}
.slip .side{position:absolute;left:0;top:0;width:400px;height:100%;background:var(--ink);overflow:hidden}
.slip .side .mark-square{position:absolute;left:250px;top:90px;width:100px;height:100px;background:var(--gold)}
.slip .side .wordmark{position:absolute;left:0;right:0;top:250px}
.slip .side .top{font-size:56px;letter-spacing:5px;padding-left:5px}
.slip .side .bottom{font-size:38px;letter-spacing:13px;padding-left:13px;margin-top:6px}
.slip .side-band{position:absolute;left:0;bottom:0;width:400px;height:40px;background:linear-gradient(90deg,var(--gold-light),var(--gold-dark))}
.slip .greeting{position:absolute;left:400px;right:0;top:250px;text-align:center;font-size:26px;color:var(--text-dark)}
.slip .footer{position:absolute;left:450px;right:20px;bottom:48px;display:flex;justify-content:space-between;font-size:14px;color:var(--text-dark)}
.slip .footer .icon{width:18px;height:18px}
.slip .footer-rule{position:absolute;left:400px;right:0;bottom:40px;height:1px;background:var(--line)}
</style>
</head>
<body>
<svg width="0" height="0" style="position:absolute">
  <defs>
    <symbol id="i-phone" viewBox="0 0 20 20"><circle cx="10" cy="10" r="10" fill="#a8a46a"/><path d="M7 5l2 2-1 1.5a7 7 0 0 0 3.5 3.5L13 11l2 2-1.5 1.5C9 14 6 11 5.5 6.5z" fill="#3d3835"/></symbol>
    <symbol id="i-pin" viewBox="0 0 20 20"><circle cx="10" cy="10" r="10" fill="#a8a46a"/><path d="M10 4a4 4 0 0 0-4 4c0 3 4 8 4 8s4-5 4-8a4 4 0 0 0-4-4zm0 5.5a1.5 1.5 0 1 1 0-3 1.5 1.5 0 0 1 0 3z" fill="#3d3835"/></symbol>
    <symbol id="i-mail" viewBox="0 0 20 20"><circle cx="10" cy="10" r="10" fill="#a8a46a"/><path d="M5 6.5h10v7H5z" fill="#3d3835"/><path d="M5 6.5l5 4 5-4" fill="none" stroke="#a8a46a" stroke-width="1"/></symbol>
    <symbol id="i-web" viewBox="0 0 20 20"><circle cx="10" cy="10" r="10" fill="#a8a46a"/><circle cx="10" cy="10" r="5" fill="none" stroke="#3d3835" stroke-width="1.3"/><path d="M5 10h10M10 5c-2 3-2 7 0 10M10 5c2 3 2 7 0 10" fill="none" stroke="#3d3835" stroke-width="1"/></symbol>
  </defs>
</svg>

<section class="brand-panel">
  <div class="mark-square"></div>
  <div class="wordmark"><span class="top">Halvorn</span><span class="bottom">Group</span></div>
</section>

<section class="card-scene">
  <article class="card card-front">
    <div class="mini-square"></div>
    <p class="name">YOUR NAME</p>
    <p class="role">Manager</p>
    <div class="contact-stack">
      <div class="item"><svg class="icon"><use href="#i-phone"/></svg>321 555 01847</div>
      <div class="item"><svg class="icon"><use href="#i-pin"/></svg><em>po box, city, state, zip</em></div>
      <div class="item"><svg class="icon"><use href="#i-mail"/></svg>hello@halvorngroup.com</div>
      <div class="item"><svg class="icon"><use href="#i-web"/></svg>halvorngroup.com</div>
    </div>
    <div class="band"></div>
  </article>
  <article class="card card-back">
    <div class="mark-square"></div>
    <div class="wordmark"><span class="top">Halvorn</span><span class="bottom">Group</span></div>
    <div class="band"></div>
  </article>
</section>

<section class="letterhead-panel">
  <article class="letterhead letterhead-a">
    <div class="tab"><div class="mark-square"></div><div class="wordmark"><span class="top">Halvorn</span><span class="bottom">Group</span></div></div>
    <div class="footer">
      <span class="item"><svg class="icon"><use href="#i-phone"/></svg>321 555 01847</span>
      <span class="item"><svg class="icon"><use href="#i-pin"/></svg>po box, city, zip</span>
      <span class="item"><svg class="icon"><use href="#i-mail"/></svg>hello@halvorngroup.com</span>
      <span class="item"><svg class="icon"><use href="#i-web"/></svg>www.halvorngroup.com</span>
    </div>
    <div class="footer-rule"></div>
  </article>
  <article class="letterhead letterhead-b">
    <div class="tab"><div class="mark-square"></div><div class="wordmark"><span class="top">Halvorn</span><span class="bottom">Group</span></div></div>
    <div class="footer">
      <span class="item"><svg class="icon"><use href="#i-phone"/></svg>321 555 01847</span>
      <span class="item"><svg class="icon"><use href="#i-pin"/></svg>po box, city, zip</span>
      <span class="item"><svg class="icon"><use href="#i-mail"/></svg>hello@halvorngroup.com</span>
      <span class="item"><svg class="icon"><use href="#i-web"/></svg>www.halvorngroup.com</span>
    </div>
    <div class="footer-rule"></div>
  </article>
</section>

<article class="slip">
  <div class="side">
    <div class="mark-square"></div>
    <div class="wordmark"><span class="top">Halvorn</span><span class="bottom">Group</span></div>
  </div>
  <div class="side-band"></div>
  <p class="greeting">With Best Compliments</p>
  <div class="footer-rule"></div>
  <div class="footer">
    <span class="item"><svg class="icon"><use href="#i-phone"/></svg>321 555 01847</span>
    <span class="item"><svg class="icon"><use href="#i-pin"/></svg>po box, city, state, zip</span>
    <span class="item"><svg class="icon"><use href="#i-mail"/></svg>hello@halvorngroup.com</span>
    <span class="item"><svg class="icon"><use href="#i-web"/></svg>www.halvorngroup.com</span>
  </div>
</article>
</body>
</html>
```